Web Design Project for Wren Nectar

We are a Honey Packing Company called Wren Nectar.
We need a new website.
We are open to many ideas.
We want to have headings like: Home/Products/About Us/Contact Us
We want an easy and uncomplicated website.
We need our logo attached to the center top or left top of the webpage.
We want to have a number of our products on the first page that increase in size once the cursor is placed on them.
We want to be able to add photos and products in the future as we expand.
Updates
Target Market(s)
Public
Food Distributors
Importers/Exporters
Industry/Entity Type
It Company
Look and feel
Each slider illustrates characteristics of the customer's brand and the style your logo design should communicate.

```html
<!DOCTYPE html>
<html lang="en">
<head>
<meta charset="utf-8">
<title>Wren Nectar</title>
<link rel="stylesheet" href="https://fonts.googleapis.com/css2?family=Arimo:wght@400;700&family=PT+Sans:wght@400;700&family=PT+Sans+Narrow:wght@700&display=swap">
<style>
:root{
  --honey:#f6a81c;
  --honey-light:#fcc83a;
  --honey-deep:#e8930d;
  --cream:#fbf6cf;
  --cream-2:#f3ef9a;
  --charcoal:#2a2a2a;
  --charcoal-2:#333;
  --ink:#1f1f1f;
  --muted:#c9c9c9;
  --white:#fff;
  --heading:#f0a020;
}
*{box-sizing:border-box;margin:0;padding:0}
html,body{width:960px;height:1200px;overflow:hidden}
body{position:relative;background:var(--white);font-family:"Arimo",Arial,sans-serif;color:var(--ink)}
.abs{position:absolute}

.top-band{left:0;top:0;width:960px;height:152px;background:linear-gradient(180deg,#fffef4 0%,var(--cream) 40%,var(--cream-2) 100%)}
.nav-band{left:0;top:152px;width:960px;height:61px;background:linear-gradient(180deg,var(--honey-light),var(--honey) 60%,var(--honey-deep));border-bottom:1px solid #c77b06}

.brand{left:107px;top:0;width:158px;height:180px;display:flex;align-items:center;justify-content:center;gap:8px;flex-direction:column}
.brand-mark{width:22px;height:22px;background:var(--charcoal)}
.brand-name{font-family:"PT Sans",sans-serif;font-weight:700;font-size:28px;line-height:30px;color:var(--charcoal);text-align:center}

.mascot{left:605px;top:25px;width:86px;height:115px;border-radius:40px;background:radial-gradient(circle at 50% 40%,#f7c84a,#c9962a 70%,#7a6a55)}
.call{left:703px;top:62px;font-family:"PT Sans",sans-serif;color:var(--ink)}
.call-label{font-size:15px;line-height:20px}
.call-number{font-size:27px;line-height:30px}

.main-nav{left:355px;top:143px;height:78px;display:flex}
.main-nav a{display:flex;align-items:center;height:70px;margin-top:9px;padding:0 11px;font-family:"PT Sans",sans-serif;font-size:13px;color:var(--ink);text-decoration:none;border-left:1px solid #b36f05}
.main-nav a:first-child{border-left:none}
.main-nav a.active{background:var(--charcoal);color:var(--white);margin-top:0;height:78px;padding:0 12px}

.hero{left:104px;top:224px;width:752px;height:326px;border-radius:10px;overflow:hidden;border:1px solid #999;
  background:linear-gradient(90deg,#5b5644 0%,#8d886f 35%,#b8934a 62%,#e39b1c 75%,#4b4533 100%)}
.hero-title{left:64px;top:104px;font-family:"PT Sans Narrow",sans-serif;font-weight:700;font-size:50px;line-height:56px;color:var(--white);letter-spacing:-0.5px;text-shadow:0 2px 4px rgba(0,0,0,.35)}
.hero-arrow{top:139px;width:46px;height:46px;background:var(--charcoal);display:flex;align-items:center;justify-content:center}
.hero-arrow.prev{left:0}
.hero-arrow.next{right:0}

.card{top:565px;width:240px;height:295px;background:var(--charcoal);border-radius:6px;overflow:hidden}
.card-head{height:40px;background:linear-gradient(180deg,var(--honey-light),var(--honey));text-align:center;font-family:"PT Sans",sans-serif;font-size:22px;line-height:42px;color:var(--ink)}
.card-lead{margin:14px 14px 0;font-size:12px;font-weight:700;color:var(--white)}
.card-text{margin:4px 14px 0;font-size:11.5px;line-height:20px;color:var(--muted)}
.card-photo{position:absolute;left:12px;top:123px;width:217px;height:110px;border:2px solid #e8e8e8}
.btn-light{position:absolute;left:54px;top:248px;width:132px;height:33px;border-radius:6px;background:linear-gradient(180deg,#fff,#d7d7d7);font-family:"PT Sans",sans-serif;font-size:16px;line-height:33px;text-align:center;color:var(--ink)}

.section-title{font-family:"PT Sans",sans-serif;font-size:25px;color:var(--heading)}
.welcome{left:104px;top:888px;width:495px}
.welcome p{margin-top:14px;font-size:11px;line-height:18.5px;color:var(--ink)}
.btn-dark{left:104px;top:1054px;width:133px;height:33px;border-radius:6px;background:linear-gradient(180deg,#666,#2b2b2b);color:var(--white);font-family:"PT Sans",sans-serif;font-size:16px;line-height:33px;text-align:center}

.testimonials{left:616px;top:888px;width:240px}
.quote{position:absolute;left:0;width:240px}
.avatar{position:absolute;left:0;top:0;width:64px;height:64px;border:1px solid #999;border-radius:8px;background:linear-gradient(180deg,#eef2f5,#b9c3cc)}
.quote-name{position:absolute;left:77px;top:0;font-size:11px;font-weight:700}
.quote-text{position:absolute;left:77px;top:16px;width:163px;font-size:11px;line-height:18px}

.footer{left:104px;top:1112px;width:752px;height:71px;background:var(--charcoal);border-radius:10px;color:var(--white)}
.footer-copy{position:absolute;left:21px;top:20px;font-family:"PT Sans",sans-serif;font-size:11px;line-height:15px}
.follow{position:absolute;left:557px;top:25px;display:flex;align-items:center;gap:6px;font-family:"PT Sans",sans-serif;font-size:13px}
.social{width:26px;height:26px;border-radius:4px;background:linear-gradient(180deg,#ddd,#999)}
.bottom-stripe{left:0;top:1190px;width:960px;height:10px;background:var(--honey-light)}
</style>
</head>
<body>
<div class="abs top-band" role="img" aria-label="Soft honeycomb pattern in pale yellow"></div>
<div class="abs nav-band"></div>

<div class="abs brand">
  <span class="brand-mark"></span>
  <span class="brand-name">Wren<br>Nectar</span>
</div>

<div class="abs mascot" role="img" aria-label="Cartoon bee mascot holding a spanner"></div>
<div class="abs call">
  <div class="call-label">Call Us:</div>
  <div class="call-number">123 555 0147</div>
</div>

<nav class="abs main-nav">
  <a class="active" href="#">Home</a>
  <a href="#">About Us</a>
  <a href="#">Products</a>
  <a href="#">Services</a>
  <a href="#">Pricing</a>
  <a href="#">Our Dealers</a>
  <a href="#">Contact Us</a>
</nav>

<section class="abs hero" role="img" aria-label="Three squeeze bottles of honey in front of a bowl of honey with a dipper">
  <h1 class="abs hero-title">Healthy Bee<br>Pure Honey</h1>
  <div class="abs hero-arrow prev"><svg width="12" height="14"><path d="M10 0 L0 7 L10 14Z" fill="#fff"/></svg></div>
  <div class="abs hero-arrow next"><svg width="12" height="14"><path d="M2 0 L12 7 L2 14Z" fill="#fff"/></svg></div>
</section>

<article class="abs card" style="left:104px">
  <div class="card-head">Products Gallery</div>
  <p class="card-lead">Sed ut perspiciatis unde omnis</p>
  <p class="card-text">Linior voluptatm accusantium doloremque laudantium totarem aperiam.</p>
  <div class="card-photo" role="img" aria-label="Jar of honey on a white background" style="background:linear-gradient(90deg,#fafafa 30%,#e88a1c 45%,#f2a02a 55%,#fafafa 70%)"></div>
  <div class="btn-light">View All Products</div>
</article>
<article class="abs card" style="left:360px">
  <div class="card-head">Products Storage</div>
  <p class="card-lead">Sed ut perspiciatis unde omnis</p>
  <p class="card-text">Linior voluptatm accusantium doloremque laudantium totarem aperiam.</p>
  <div class="card-photo" role="img" aria-label="Warehouse with stacked honey storage containers" style="background:linear-gradient(180deg,#c9c6bd,#e6e4dc 50%,#8f8b80)"></div>
  <div class="btn-light">Read More</div>
</article>
<article class="abs card" style="left:616px">
  <div class="card-head">Products Quality</div>
  <p class="card-lead">Sed ut perspiciatis unde omnis</p>
  <p class="card-text">Linior voluptatm accusantium doloremque laudantium totarem aperiam.</p>
  <div class="card-photo" role="img" aria-label="Honey dipper resting in a jar of honey" style="background:linear-gradient(160deg,#f6b043,#d86a0c 60%,#f4f0ea)"></div>
  <div class="btn-light">Read More</div>
</article>

<section class="abs welcome">
  <h2 class="section-title">Welcome to Our Site !</h2>
  <p>Neque porro quisquam est, qui dolorem ipsum quia dolor sit amet, consectetur, adipisci velit, sed quia non numquam eius modi tempora incidunt ut labore et dolore magnam aliquam quaerat voluptatemt enim ad minima veniam, quis nostrum exercitationem. Neque porro quisquam est, qui dolorem ipsum quia dolor sit amet, consectetur, adipisci velit, sed quia non numquam eius modi tempora incidunt ut labore et dolore magnam aliquam quaerat voluptatemt enim ad minima veniam, quis nostrum exercitationem.</p>
</section>
<div class="abs btn-dark">Read More</div>

<section class="abs testimonials">
  <h2 class="section-title">Clients Testimonials</h2>
  <div class="quote" style="top:50px">
    <div class="avatar" role="img" aria-label="Portrait placeholder of a client in a suit"></div>
    <div class="quote-name">Marcus Hale</div>
    <div class="quote-text">Lorem ipsum dolor sitmet con-sectetur adipisicing elit sed do eiusmod.</div>
  </div>
  <div class="quote" style="top:135px">
    <div class="avatar" role="img" aria-label="Portrait placeholder of a client"></div>
    <div class="quote-name">Nina Corbel</div>
    <div class="quote-text">Tempor incididunt utlabore et dolore magna aliqua ut enim ad minim veniam.</div>
  </div>
</section>

<footer class="abs footer">
  <div class="footer-copy">© Copyright 2012 &nbsp;by &nbsp;Wren Nectar. All Rights Reserved<br>Privacy Policy</div>
  <div class="follow">Follow &nbsp;us on : <span class="social"></span><span class="social"></span><span class="social"></span></div>
</footer>
<div class="abs bottom-stripe"></div>
</body>
</html>
```